Ice cream manufacturer need packaging design

We are a artisanal ice cream maker - Gelato makers - we are in the process of commercialising our products to restaurants, hotels. catering services and large supermarkets. It is a unique product which we are bringing to the market as it is a traditionally made ice cream using fresh ingredients rather than flavouring. We will be selling our products in small individual containers of 100ml as well as family boxes of 500ml and 1l. A little bit like Brellovin.We need the packaging to ooze quality, it needs to scream that' this is not your average industrial air full ice cream, but quality natural ingredients'The packaging needs to include:- The brand name Plenta as a nice logo- The flavour- Ingredients section.- Batch number- Expire date (should read see lid)- The name and address of the manufacturer - Sweet Harbor, Rue Kamel Ferhani, Draria, Alger, Algerie - Special storage conditions - To be stored at -18 degrees and left at room temperature for 10 min before consumption.- Net weight: 100ml or 500ml or 1l

Industry/Entity Type

Food Production

Colors

Designer to choose colors to be used in the design.

Requirements
Must have
• Brand Name and Flavour with some reference to ice cream.
Nice to have
• It must convey that this is a quality product.
Should not have
• It should not have a funny or playful message

```html
<!DOCTYPE html>
<html lang="en">
<head>
<meta charset="utf-8">
<title>Plenta Premium Ice Cream – Tub Label</title>
<link rel="stylesheet" href="https://fonts.googleapis.com/css2?family=Oswald:wght@500;700&display=swap">
<style>
  :root {
    --backdrop: #e6e6e6;
    --teal-light: #1ba8a0;
    --teal: #13938d;
    --teal-deep: #0b6b69;
    --gold: #c9a91a;
    --gold-deep: #8a6d0c;
    --berry: #b0173d;
    --berry-deep: #7a0d2a;
    --ink-light: #ffffff;
    --ink-soft: #f1efe2;
  }
  html, body {
    margin: 0;
    padding: 0;
    width: 1200px;
    height: 960px;
    overflow: hidden;
    background: var(--backdrop);
    font-family: "Oswald", "Arial Narrow", sans-serif;
  }
  .canvas {
    position: relative;
    width: 1200px;
    height: 960px;
  }

  /* Side wrap label */
  .side-label {
    position: absolute;
    left: 70px;
    top: 120px;
    width: 600px;
    height: 720px;
    overflow: hidden;
    background: radial-gradient(ellipse at 45% 35%, var(--teal-light) 0%, var(--teal) 45%, var(--teal-deep) 100%);
    box-shadow: 0 10px 30px rgba(0,0,0,0.18);
  }
  .side-label .gold-band {
    position: absolute;
    inset: 0;
    width: 100%;
    height: 100%;
  }

  /* Round lid label */
  .lid-label {
    position: absolute;
    left: 730px;
    top: 230px;
    width: 420px;
    height: 420px;
    border-radius: 50%;
    overflow: hidden;
    background: radial-gradient(circle at 45% 40%, var(--teal-light) 0%, var(--teal) 50%, var(--teal-deep) 100%);
    box-shadow: 0 10px 30px rgba(0,0,0,0.18), inset 0 0 0 14px var(--gold);
  }
  .lid-label .gold-band {
    position: absolute;
    inset: 0;
    width: 100%;
    height: 100%;
  }

  .brand-block {
    position: absolute;
    text-align: left;
  }
  .brand-name {
    display: block;
    margin: 0;
    font-weight: 700;
    color: var(--ink-light);
    line-height: 1;
    letter-spacing: 1px;
  }
  .brand-tagline {
    display: block;
    margin: 0;
    font-weight: 500;
    color: var(--ink-soft);
    letter-spacing: 0.5px;
  }

  .scoops-visual {
    position: absolute;
    border-radius: 50%;
    background: radial-gradient(circle at 40% 40%, var(--berry) 0%, var(--berry-deep) 75%);
  }

  .pack-info {
    position: absolute;
    text-align: center;
    color: var(--ink-soft);
    font-weight: 700;
    line-height: 1.05;
  }

  /* side positions */
  .side-label .brand-block { left: 150px; top: 110px; }
  .side-label .brand-name { font-size: 92px; }
  .side-label .brand-tagline { font-size: 24px; margin-top: 6px; }
  .side-label .scoops-visual { left: 170px; top: 310px; width: 270px; height: 200px; border-radius: 48%; }
  .side-label .pack-info { left: 0; right: 0; top: 560px; font-size: 40px; }

  /* lid positions */
  .lid-label .brand-block { left: 92px; top: 48px; }
  .lid-label .brand-name { font-size: 56px; }
  .lid-label .brand-tagline { font-size: 15px; margin-top: 2px; }
  .lid-label .scoops-visual { left: 120px; top: 165px; width: 180px; height: 120px; border-radius: 48%; }
  .lid-label .pack-info { left: 0; right: 0; top: 300px; font-size: 26px; }
</style>
</head>
<body>
<main class="canvas">

  <section class="side-label" aria-label="Tub side label">
    <svg class="gold-band" viewBox="0 0 600 720" preserveAspectRatio="none" aria-hidden="true">
      <defs>
        <linearGradient id="bandGold" x1="0" y1="0" x2="1" y2="0">
          <stop offset="0" stop-color="#d8b920"/>
          <stop offset="1" stop-color="#8a6d0c"/>
        </linearGradient>
      </defs>
      <path d="M0 0 H600 V190 C470 190 420 230 380 260 C330 150 180 120 0 150 Z" fill="url(#bandGold)"/>
      <path d="M0 150 C180 120 330 150 380 260" fill="none" stroke="#5a3a12" stroke-width="3"/>
    </svg>
    <div class="brand-block">
      <span class="brand-name">Plenta</span>
      <span class="brand-tagline">Premium Ice cream</span>
    </div>
    <div class="scoops-visual" role="img" aria-label="Photo of two scoops of red berry sorbet with a white cream swirl"></div>
    <div class="pack-info">
      <div class="pack-size">150 ml</div>
      <div class="pack-flavour">Natral</div>
    </div>
  </section>

  <section class="lid-label" aria-label="Tub lid label">
    <svg class="gold-band" viewBox="0 0 420 420" preserveAspectRatio="none" aria-hidden="true">
      <path d="M230 0 H420 V150 C360 140 320 150 290 165 C280 110 260 60 230 0 Z" fill="#b89a16"/>
    </svg>
    <div class="brand-block">
      <span class="brand-name">Plenta</span>
      <span class="brand-tagline">Premium Ice cream</span>
    </div>
    <div class="scoops-visual" role="img" aria-label="Photo of two scoops of red berry sorbet with a white cream swirl"></div>
    <div class="pack-info">
      <div class="pack-size">150 ml</div>
      <div class="pack-flavour">Natral</div>
    </div>
  </section>

</main>
</body>
</html>
```